Every sort of trades everysortoftrades.ca

Website for company offering Every sort of trades
Welding/Fabrication/Metal repairs/Metal building, Electrical repairs and installations, Plumbing and Heating, Renovations, Flooring, Paiting, and other services

We need a very clean and professional website outlining the many services we have

We would like each type of service to have its own page, with images of those types of services on those pages.

Then in the future, we can update those pages with projects we have done of those types.

Every Sort of Trades . CA

Located in Calgary, Alberta, Canada, offering services Alberta wide

Welding/Fabrication/Repair/Building - Steel and metals
Electrical contractor - Journeyman , small or large projects
Plumbing and Heating
Renovations
Flooring
Painting
Other services - storage, trucking, delivery, etc

business and residential services

Contractor

5+ page

Sans Serif

3176b5
0253a1
85acd3
85abd2
cedeed
ffffff

Must have
• Clean
• Professional
• Easy of updating text and images

```html
<!DOCTYPE html>
<html lang="en">
<head>
<meta charset="utf-8">
<title>Every Sort of Trades</title>
<link href="https://fonts.googleapis.com/css2?family=Roboto:ital,wght@0,400;0,500;0,700;1,400&display=swap" rel="stylesheet">
<style>
:root{
  --blue:#0253a1;
  --blue-mid:#3176b5;
  --blue-soft:#85acd3;
  --blue-pale:#cedeed;
  --white:#ffffff;
  --ink:#222831;
  --grey:#555b63;
  --band:#f1f4f8;
}
*{box-sizing:border-box;margin:0;padding:0}
html,body{width:1200px;height:2368px;overflow:hidden}
body{position:relative;font-family:'Roboto',Arial,sans-serif;color:var(--ink);background:var(--white)}
.abs{position:absolute}
.dotted{position:absolute;left:52px;width:1096px;border-top:2px dotted var(--blue-mid)}

/* header */
.site-header{position:absolute;left:0;top:0;width:1200px;height:74px;border-top:4px solid var(--blue);background:var(--white)}
.logo{position:absolute;left:52px;top:14px;font-size:32px;font-weight:400;color:var(--blue);letter-spacing:1px}
.main-nav{position:absolute;left:426px;top:26px;display:flex;gap:37px;font-size:14px;font-weight:500;color:var(--ink)}
.chat{position:absolute;left:980px;top:26px;font-size:13px;font-weight:500}
.btn-estimate{position:absolute;left:1040px;top:16px;width:113px;height:33px;border-radius:5px;background:var(--blue);color:var(--white);font-size:13px;font-weight:700;display:flex;align-items:center;justify-content:center}

/* hero */
.hero{position:absolute;left:0;top:74px;width:1200px;height:486px;background:linear-gradient(180deg,#d9dcdf 0%,#c9cdc9 30%,#7f9a5f 55%,#4f7d2e 100%)}

/* welcome */
.section-title{position:absolute;left:0;width:1200px;text-align:center;font-size:22px;font-weight:500;color:var(--ink)}
.section-title span{color:var(--blue)}
.intro{position:absolute;left:80px;top:624px;width:1040px;text-align:center;font-size:12.5px;line-height:19px;color:var(--grey)}

/* services */
.services{position:absolute;left:0;top:671px;width:1200px;height:329px;background:linear-gradient(180deg,#eef2f6,#f5f7fa)}
.tabs{position:absolute;left:62px;top:16px;display:flex;align-items:center;font-size:14.5px;font-weight:500}
.tab{height:44px;display:flex;align-items:center;padding:0 18px;margin-right:16px;border:1px solid transparent;border-radius:4px}
.tab.active{border-color:var(--blue-mid);color:var(--blue);background:var(--white);padding:0 19px}
.card{position:absolute;top:133px;width:253px;height:147px}
.card-photo{position:absolute;left:0;top:0;width:253px;height:122px;border-radius:6px}
.card-icon{position:absolute;left:103px;top:-24px;width:48px;height:48px;border-radius:50%;background:var(--blue);border:3px solid var(--white);display:flex;align-items:center;justify-content:center}
.card-label{position:absolute;left:11px;top:104px;width:231px;height:43px;border-radius:4px;background:linear-gradient(180deg,#3176b5,#0253a1);color:var(--white);font-size:15.5px;display:flex;align-items:center;justify-content:center}

/* projects */
.project{position:absolute;top:1067px;width:240px;height:179px}

/* testimonials */
.testimonials{position:absolute;left:0;top:1276px;width:1200px;height:361px;background:linear-gradient(180deg,#eef1f5,#f7f8fa)}
.quote{position:absolute;width:400px;font-size:12.5px;line-height:19px;font-style:italic;color:var(--grey)}
.quote.left{text-align:right}
.quote .who{display:block;margin-top:12px;font-style:normal;color:var(--ink);font-size:12.5px}
.avatar{position:absolute;width:74px;height:74px;border-radius:50%;background:linear-gradient(180deg,#bfb3a6,#6f6a66);border:3px solid var(--white)}

/* process */
.step{position:absolute;top:1717px;width:95px;height:95px;border-radius:50%;background:var(--blue);display:flex;align-items:center;justify-content:center}
.step.current{box-shadow:0 0 0 4px var(--white),0 0 0 7px var(--blue)}
.connector{position:absolute;top:1764px;width:96px;border-top:2px solid var(--blue-soft)}
.step-label{position:absolute;top:1836px;width:224px;text-align:center;font-size:15px;font-weight:500}
.step-label.current{color:var(--blue)}

/* footer */
.skyline{position:absolute;left:0;top:1887px;width:1200px;height:77px;background:linear-gradient(180deg,rgba(2,83,161,0),rgba(2,83,161,.55))}
.site-footer{position:absolute;left:0;top:1964px;width:1200px;height:404px;background:linear-gradient(160deg,#0253a1,#3176b5);color:var(--white)}
.f-title{position:absolute;top:22px;font-size:17px;font-weight:500}
.f-text{position:absolute;font-size:12.5px;line-height:20px}
.f-text p{margin-bottom:13px}
.socials{position:absolute;left:52px;top:250px;display:flex;gap:12px}
.socials i{width:12px;height:12px;border-radius:50%;background:var(--white);display:block}
.map{position:absolute;left:333px;top:65px;width:534px;height:218px;background:linear-gradient(135deg,#b9d3ef,#e6ebe6 55%,#d8e2cf)}
.f-rule{position:absolute;left:52px;top:336px;width:1096px;border-top:1px solid rgba(255,255,255,.45)}
.copy{position:absolute;top:366px;font-size:11px;font-weight:500}
.f-logo{position:absolute;left:0;top:356px;width:1200px;text-align:center;font-size:30px;letter-spacing:1px}
</style>
</head>
<body>

<header class="site-header">
  <div class="logo">LOGO</div>
  <nav class="main-nav"><span>Our Company</span><span>Services</span><span>Project</span><span>Contact</span></nav>
  <div class="chat">Chat
    <svg width="12" height="10" viewBox="0 0 12 10"><path d="M1 1h10v6H5l-3 2V7H1z" fill="none" stroke="#222831" stroke-width="1.4"/></svg>
  </div>
  <div class="btn-estimate">Free Estimates</div>
</header>

<div class="hero" role="img" aria-label="Cutaway wooden house with water tank standing on a green field under a misty sky"></div>

<h1 class="section-title" style="top:563px">Welcome to <span>Everysortof</span></h1>
<div class="dotted" style="top:601px"></div>
<p class="intro">Sed ut perspiciatis unde omnis iste natus error sit voluptatem accusantium doloremque laudantium, totam rem aperiam, eaque ipsa quae ab illo inventore veritatis et quasi architecto beatae vitae dicta sunt explicabo.</p>

<section class="services">
  <div class="tabs">
    <div class="tab active">Steel and metals</div>
    <div class="tab">Electrical contractor</div>
    <div class="tab">Plumbing and Heating</div>
    <div class="tab">Renovations</div>
    <div class="tab">Flooring</div>
    <div class="tab">Painting</div>
    <div class="tab">Other services</div>
  </div>
  <div class="dotted" style="top:76px"></div>

  <div class="card" style="left:52px">
    <div class="card-photo" role="img" aria-label="Welder at work with mask and sparks" style="background:linear-gradient(135deg,#1c2550,#4a5aa0 60%,#2a2f55)"></div>
    <div class="card-icon"><svg width="22" height="22" viewBox="0 0 22 22"><rect x="5" y="3" width="12" height="12" rx="3" fill="#fff"/><rect x="7" y="7" width="8" height="3" fill="#0253a1"/><rect x="4" y="16" width="14" height="3" rx="1" fill="#fff"/></svg></div>
    <div class="card-label">Welding</div>
  </div>
  <div class="card" style="left:332px">
    <div class="card-photo" role="img" aria-label="Fabricated concrete structure on a site" style="background:linear-gradient(135deg,#5f7261,#c9ced0 50%,#e6e8ea)"></div>
    <div class="card-icon"><svg width="22" height="22" viewBox="0 0 22 22"><path d="M3 4h16v4h-6v10H9V8H3z" fill="#fff"/></svg></div>
    <div class="card-label">Fabrication</div>
  </div>
  <div class="card" style="left:612px">
    <div class="card-photo" role="img" aria-label="Copper pipe being repaired with a torch beside a shower" style="background:linear-gradient(135deg,#d8c9a8,#b98a55 45%,#6fa0cf)"></div>
    <div class="card-icon"><svg width="22" height="22" viewBox="0 0 22 22"><rect x="3" y="7" width="16" height="11" rx="1" fill="#fff"/><rect x="8" y="4" width="6" height="4" fill="none" stroke="#fff" stroke-width="2"/><rect x="10" y="10" width="2" height="5" fill="#0253a1"/></svg></div>
    <div class="card-label">Repair</div>
  </div>
  <div class="card" style="left:892px">
    <div class="card-photo" role="img" aria-label="Steel frame building under construction with cranes" style="background:linear-gradient(180deg,#4d74b8,#8fa9d2 55%,#6b6f75)"></div>
    <div class="card-icon"><svg width="22" height="22" viewBox="0 0 22 22"><path d="M2 10L11 3l9 7v9H2z" fill="#fff"/><rect x="6" y="12" width="10" height="2" fill="#0253a1"/><rect x="6" y="15" width="10" height="2" fill="#0253a1"/></svg></div>
    <div class="card-label">Building</div>
  </div>
</section>

<h2 class="section-title" style="top:1005px">Latest <span>Projects</span></h2>
<div class="dotted" style="top:1044px"></div>
<div class="project" style="left:0;background:linear-gradient(180deg,#2a5fa8,#3b3e4a 65%,#1c1d22)" role="img" aria-label="Modern house with lit terrace at dusk"></div>
<div class="project" style="left:240px;background:linear-gradient(180deg,#3a3e48,#5b5a55 55%,#3d5a2e)" role="img" aria-label="Contemporary home with pool and lawn"></div>
<div class="project" style="left:480px;background:linear-gradient(180deg,#9aa4b3,#6a5a4a 55%,#4a4a48)" role="img" aria-label="Two storey house entrance with walkway"></div>
<div class="project" style="left:720px;background:linear-gradient(180deg,#c88a4a,#8a5a33 55%,#b49070)" role="img" aria-label="Warm wooden living room interior"></div>
<div class="project" style="left:960px;background:linear-gradient(180deg,#4f74b8,#8faad6 50%,#6f7f5f)" role="img" aria-label="Single storey home with garage and lawn"></div>

<section class="testimonials" role="region" aria-label="Testimonials">
  <h2 class="section-title" style="top:16px">What <span>People Say</span></h2>
  <div class="dotted" style="top:57px"></div>
  <div class="abs" style="left:599px;top:100px;height:240px;border-left:2px dotted var(--blue-mid)"></div>
  <div class="dotted" style="top:211px"></div>

  <p class="quote left" style="left:62px;top:96px">Duis aute irure dolor in reprehenderit in voluptate velit esse cillum dolore eu fugiat nulla pariatur. Excepteur sint occaecat cupidatat non proident, sunt in culpa qui officia deserunt mollit.<span class="who">Derek Colter, Operations Manager</span></p>
  <div class="avatar" style="left:491px;top:104px" role="img" aria-label="Portrait of Derek Colter"></div>

  <div class="avatar" style="left:634px;top:104px" role="img" aria-label="Portrait of Lena Graves"></div>
  <p class="quote" style="left:739px;top:96px">Provident, similique sunt in culpa qui officia deserunt mollitia animi, id est laborum et dolorum fuga. Et harum quidem rerum facilis est et expedita distinctio. Nam libero tempore, cum soluta nobis.<span class="who">Lena Graves, Creative Designer</span></p>

  <p class="quote left" style="left:62px;top:236px">Luis aute irure dolor in reprehenderit in piluptate velit esse cillum dolore eu fugiat nulla pariatur. Excepteur sint occaecat cupidatat non proident, sunt in culpa qui officia deserunt mollit.<span class="who">Marla Leigh, Manager</span></p>
  <div class="avatar" style="left:491px;top:243px" role="img" aria-label="Portrait of Marla Leigh"></div>

  <div class="avatar" style="left:634px;top:243px" role="img" aria-label="Portrait of Tim Larkin"></div>
  <p class="quote" style="left:739px;top:236px">At vero eos et accusamus et iusto odio dignissimos ducimus qui blanditiis praesentium voluptatum deleniti atque corrupti quos dolores et quas molestias excepturi sint occaecati asperiores.<span class="who">Tim Larkin, Developer</span></p>
</section>

<h2 class="section-title" style="top:1650px">Our <span>Process</span></h2>
<div class="dotted" style="top:1689px"></div>

<div class="connector" style="left:216px"></div>
<div class="connector" style="left:440px"></div>
<div class="connector" style="left:664px"></div>
<div class="connector" style="left:888px"></div>

<div class="step" style="left:104px"><svg width="42" height="42" viewBox="0 0 24 24"><path d="M6.6 10.8a15 15 0 006.6 6.6l2.2-2.2a1 1 0 011-.25 11.4 11.4 0 003.6.57 1 1 0 011 1V20a1 1 0 01-1 1A17 17 0 013 4a1 1 0 011-1h3.5a1 1 0 011 1c0 1.25.2 2.45.57 3.57a1 1 0 01-.25 1z" fill="#fff"/></svg></div>
<div class="step" style="left:328px"><svg width="42" height="42" viewBox="0 0 42 42" fill="none" stroke="#fff" stroke-width="2.5"><rect x="6" y="8" width="30" height="26"/><path d="M14 8v26M14 18h22M24 18v16"/></svg></div>
<div class="step current" style="left:552px"><svg width="44" height="44" viewBox="0 0 44 44" fill="none" stroke="#fff" stroke-width="2.5"><rect x="6" y="9" width="32" height="27" rx="2"/><path d="M6 16h32M13 5v7M31 5v7M13 22h18v9H13zM22 22v9"/></svg></div>
<div class="step" style="left:776px"><svg width="44" height="44" viewBox="0 0 44 44" fill="none" stroke="#fff" stroke-width="2.5"><path d="M5 20L22 7l17 13M10 17v19h24V17M16 24h12v12H16z"/></svg></div>
<div class="step" style="left:1000px"><svg width="42" height="42" viewBox="0 0 42 42" fill="none" stroke="#fff" stroke-width="2.5"><path d="M9 5h18l6 6v26H9z"/><path d="M14 15h14M14 21h14M14 27h8M26 33l10-10"/></svg></div>

<div class="step-label" style="left:40px">Application Processing</div>
<div class="step-label" style="left:264px">Project Development</div>
<div class="step-label current" style="left:488px">Drawing up an Estimate</div>
<div class="step-label" style="left:712px">Building</div>
<div class="step-label" style="left:935px">Signing of the Act</div>

<div class="skyline" role="img" aria-label="City skyline and airport silhouette"></div>

<footer class="site-footer">
  <h3 class="f-title" style="left:52px">Contact Us</h3>
  <div class="f-text" style="left:52px;top:64px;width:255px">
    <p>Please feel free to contact us for any issue. Our staff is available to you from 9AM until 5PM on weekdays.</p>
    <p><b>Phone:</b> +1 800 555 0147</p>
    <p><b>Office:</b> Bow Valley Trade Centre</p>
    <p><b>Email:</b> info@everysortoftrades.ca</p>
  </div>
  <div class="socials"><i></i><i></i><i></i><i></i><i></i></div>

  <h3 class="f-title" style="left:333px;width:534px;text-align:center">Headquarters</h3>
  <div class="map" role="img" aria-label="Street map showing the headquarters location in Calgary"></div>

  <h3 class="f-title" style="left:895px">About Team</h3>
  <div class="f-text" style="left:895px;top:64px;width:255px">
    <p>Enim congue blandit. Lorem ipsum dolor sit amet, consectetur adipiscing elit. Quisque consectetur interdum finibus. Vestibulum ante ipsum primis in faucibus orci. luctus et ultrices posuere.</p>
    <p>Cubilia cras blandit finibus ipsum, id porttitor arcu volutpat a. Integer iaculis erat nec justo malesuada faucibus vel tempus sapien. Vivamus aliquam euismod tristique.</p>
  </div>

  <div class="f-rule"></div>
  <div class="copy" style="left:52px">Copyright © Everysortof Trades Inc</div>
  <div class="f-logo">LOGO</div>
  <div class="copy" style="right:52px">All rights reserved</div>
</footer>

</body>
</html>
```